Book cover for middle grade children's book

I need a book cover design for the first book in my middle grade series aimed at girls ages 9-12.

PLEASE SEE MY ATTACHED EXAMPLES.

Title: Pim Dorsey: Cousin Mabel's Payback

Design Brief:
Front: I want it to look like a composition book. The background should be a pink plaid design. There should be a white square in the center like a composition book. On top of the square in purple letters should be the name Pim. Underneath the square should be the name Dorsey. Pim Dorsey should be in a fun girly font that's readible on thumbnail. The sub title should go on the white square where a kid would write their name. It should say Cousin Mabel's Payback in a girl's pink handwriting. At the bottom underneath Dorsey should be my name: Rhonda Louise Barlow

On the left side there should be a dark pink or purple (whichever looks best with the pattern) strip like composition books have.

Spine: Pim Dorsey: Cousin Mabel's Payback (Pim Dorsey #1) Barlow

On the back: I'd like the back to be hot pink with white font.

Thirteen-year-old Pim Dorsey has a lot on her plate. Her biggest challenge is living with her Cousin Mabel. As much as Pim tries to please her aunt,, they always seem to butt heads. Sometimes Pim feels as if Cousin Mabel goes out of her way to make her life miserable.

Cousin Mabel enrolls Pim in a social group called the Golden Finches, a group that's supposed to teach young girls how to be proper ladies, however it turns out to be nothing more than a club for snobs. Pim wants out, but she's made a deal with Cousin Mabel. Will Pim take a stand against the Golden Finches or will their snobbery rub off on her?
IT'S VERY IMPORTANT THAT IT LOOKS LIKE A COMPOSITION BOOK SINCE THAT WILL BE THE BRAND FOR THE SERIES.

I need this cover to fit the mandates for ebook and pressnook. Place follow the correct measurements.

This book will be 160 pages on cream paper. 6x9

Target Market(s)

Girls ages 9 and up

Industry/Entity Type

Club

Requirements
Must have
• Readable professional looking font
Should not have
• A background pattern that too busy and clashes with the font

```html
<!DOCTYPE html>
<html lang="en">
<head>
<meta charset="UTF-8">
<title>Pim Dorsey: Cousin Mabel's Payback — Cover Spread</title>
<link href="https://fonts.googleapis.com/css2?family=Dancing+Script:wght@500;700&family=Ribeye&display=swap" rel="stylesheet">
<style>
  :root {
    --page-bg: #ffffff;
    --back-dark: #b3154b;
    --back-light: #ad5677;
    --front-dark: #d84f80;
    --front-light: #e399b6;
    --spine: #9b0b60;
    --label-bg: #ffffff;
    --label-border: #d4266f;
    --title-pink: #e3208a;
    --rule-purple: #9b0b60;
    --white: #ffffff;
  }
  * { margin: 0; padding: 0; box-sizing: border-box; }
  html, body {
    width: 1200px; height: 1000px; overflow: hidden;
    background: var(--page-bg);
  }
  .canvas { position: relative; width: 1200px; height: 1000px; }
  .cover-spread {
    position: absolute; left: 86px; top: 95px;
    width: 1028px; height: 810px;
    display: flex;
    box-shadow: 5px 5px 10px rgba(0,0,0,0.28);
  }
  .back-cover {
    position: relative; width: 492px; height: 100%;
    background: repeating-linear-gradient(36deg,
      var(--back-dark) 0 31px, var(--back-light) 31px 62px);
  }
  .blurb {
    position: absolute; left: 24px; top: 44px; width: 446px;
    color: var(--white);
    font-family: "Dancing Script", cursive;
    font-weight: 500; font-size: 22px; line-height: 26.5px;
    letter-spacing: 1.1px; word-spacing: 1px;
    text-align: center;
  }
  .blurb p + p { margin-top: 26px; }
  .spine {
    position: relative; width: 48px; height: 100%;
    background: var(--spine);
  }
  .spine-text {
    position: absolute; left: 50%; top: 88px;
    transform-origin: 0 0;
    transform: rotate(90deg) translateY(-50%);
    white-space: nowrap;
    color: var(--white);
    font-family: "Dancing Script", cursive;
    font-weight: 500; font-size: 27px; line-height: 1;
    letter-spacing: 1.6px; word-spacing: 2px;
  }
  .front-cover {
    position: relative; flex: 1; height: 100%;
    background: repeating-linear-gradient(36deg,
      var(--front-dark) 0 31px, var(--front-light) 31px 62px);
  }
  .name-label {
    position: absolute; left: 82px; top: 78px;
    width: 322px; height: 162px;
    background: var(--label-bg);
    border: 3px solid var(--label-border);
    border-radius: 3px;
    text-align: center;
  }
  .series-title {
    margin-top: 22px;
    font-family: "Ribeye", serif;
    font-weight: 400;
    font-size: 46px; line-height: 1.1;
    color: var(--title-pink);
    letter-spacing: 1px;
  }
  .subtitle {
    display: block;
    margin: 10px auto 0; width: 292px;
    padding-bottom: 2px;
    border-bottom: 2px dotted var(--rule-purple);
    font-family: "Dancing Script", cursive;
    font-weight: 500; font-size: 30px; line-height: 1.15;
    letter-spacing: 1.2px;
    color: var(--title-pink);
  }
  .author {
    position: absolute; left: 0; right: 0; top: 718px;
    text-align: center;
    font-family: "Dancing Script", cursive;
    font-weight: 700; font-size: 37px;
    letter-spacing: 1px;
    color: var(--white);
    text-shadow:
      2px 0 0 var(--label-border), -2px 0 0 var(--label-border),
      0 2px 0 var(--label-border), 0 -2px 0 var(--label-border),
      1.5px 1.5px 0 var(--label-border), -1.5px -1.5px 0 var(--label-border),
      1.5px -1.5px 0 var(--label-border), -1.5px 1.5px 0 var(--label-border);
  }
</style>
</head>
<body>
<div class="canvas">
  <div class="cover-spread">
    <section class="back-cover">
      <div class="blurb">
        <p>Thirteen-year-old Pim Dorsey has a lot on her plate. Her biggest challenge is living with her Cousin Mabel. As much as Pim tries to please her aunt,, they always seem to butt heads. Sometimes Pim feels as if Cousin Mabel goes out of her way to make her life miserable.</p>
        <p>Cousin Mabel enrolls Pim in a social group called the Golden Finches, a group that's supposed to teach young girls how to be proper ladies, however it turns out to be nothing more than a club for snobs. Pim wants out, but she's made a deal with Cousin Mabel. Will Pim take a stand against the Golden Finches or will their snobbery rub off on her?</p>
      </div>
    </section>
    <section class="spine">
      <div class="spine-text">Pim Dorsey: Cousin Mabel's Payback (Pim Dorsey #1) Barlow</div>
    </section>
    <section class="front-cover">
      <div class="name-label">
        <h1 class="series-title">Pim Dorsey</h1>
        <span class="subtitle">Cousin Mabel's Payback</span>
      </div>
      <div class="author">Rhonda Louise Barlow</div>
    </section>
  </div>
</div>
</body>
</html>
```